Harbourline Blinds & Shutters

It Needs to look classy as my target is the upper end of the blind market
I need a Logo design on front and description on back of what i do:
- Roller Blinds
- Vertical Blinds
- Venetian Blinds
- Plantation Shutters
- Aluminum External Shutters
and contact details
Gavin
0418527306
and
Terry
0421690358
Updates
Hi Guys,
Sorry for the no feedback but i was waiting on my logo design. But its done now i have uploaded it. so if you could take a look and send through some designs
Reason: my logo was just finished an i just uploaded it today really dont understand why my deadline has been rached foe my bizcards as it states no deadline. But please extend
Target Market(s)
People that live on the coast and are looking for classy good quality blinds and shutters
Font styles to use
Other font styles liked:
- Copperplate Gothic,open to suggestion
Look and feel
Each slider illustrates characteristics of the customer's brand and the style your logo design should communicate.

```html
<!DOCTYPE html>
<html lang="en">
<head>
<meta charset="utf-8">
<title>Harbourline Blinds &amp; Shutters — Business Card</title>
<link rel="stylesheet" href="https://fonts.googleapis.com/css2?family=Cormorant+Garamond:ital,wght@0,500;0,600;1,500&family=Cinzel:wght@500&display=swap">
<style>
  :root {
    --backdrop: #e4e4e6;
    --card-black: #0b0b0b;
    --damask-mid: #2a2a2a;
    --damask-dark: #101010;
    --gold: #d8a632;
    --gold-deep: #a8761c;
    --ink-light: #f2f2f2;
    --card-w: 520px;
    --card-h: 297px;
  }
  * { box-sizing: border-box; margin: 0; padding: 0; }
  html, body {
    width: 1200px; height: 800px; overflow: hidden;
    background: var(--backdrop);
  }
  .canvas {
    position: relative; width: 1200px; height: 800px;
    display: flex; align-items: center; justify-content: center; gap: 60px;
  }
  .card {
    position: relative; width: var(--card-w); height: var(--card-h);
    background: var(--card-black); overflow: hidden;
    box-shadow: 0 14px 30px rgba(0,0,0,.22);
  }
  .card__damask {
    position: absolute; inset: 0;
    background: radial-gradient(ellipse at 50% 45%, var(--damask-mid) 0%, var(--damask-dark) 80%);
  }
  .card__frame {
    position: absolute; inset: 0; width: 100%; height: 100%;
  }
  /* front */
  .brand {
    position: absolute; inset: 0;
    display: flex; align-items: center; justify-content: center; gap: 14px;
  }
  .brand__dot {
    width: 16px; height: 16px; border-radius: 50%; background: var(--gold);
  }
  .brand__name {
    font-family: "Cormorant Garamond", serif; font-weight: 600;
    font-size: 34px; color: var(--gold); letter-spacing: .5px;
  }
  /* back */
  .services {
    position: absolute; list-style: none;
    font-family: "Cormorant Garamond", serif; font-weight: 500; font-style: italic;
    font-size: 23px; line-height: 1.22; color: var(--ink-light);
  }
  .services--left { left: 46px; top: 42px; }
  .services--right { left: 300px; top: 118px; }
  .contact {
    position: absolute; font-family: "Cinzel", serif; font-weight: 500;
    font-size: 17px; letter-spacing: 1.5px; color: var(--ink-light);
  }
  .contact--first { left: 46px; top: 164px; }
  .contact--second { left: 250px; top: 236px; }
  .contact__phone { margin-left: 14px; }
</style>
</head>
<body>
<main class="canvas">

  <section class="card card--back" aria-label="Business card back">
    <div class="card__damask" role="img" aria-label="Dark grey damask pattern background"></div>
    <svg class="card__frame" viewBox="0 0 520 297" aria-hidden="true">
      <g fill="none" stroke="var(--gold)" stroke-width="1.5">
        <path d="M30 62 V26 H110"/>
        <path d="M490 235 V271 H410"/>
        <path d="M400 18 H470 V60"/>
      </g>
    </svg>
    <ul class="services services--left">
      <li>-Roller Blinds</li>
      <li>-Venetian Blinds</li>
      <li>-Aluminium External Shutters</li>
    </ul>
    <ul class="services services--right">
      <li>-Vertical Blinds</li>
      <li>-Plantation Shutters</li>
    </ul>
    <p class="contact contact--first">GAVIN<span class="contact__phone">0418527306</span></p>
    <p class="contact contact--second">TERRY<span class="contact__phone">0421690358</span></p>
  </section>

  <section class="card card--front" aria-label="Business card front">
    <div class="card__damask" role="img" aria-label="Dark grey damask pattern background"></div>
    <svg class="card__frame" viewBox="0 0 520 297" aria-hidden="true">
      <g fill="none" stroke="var(--gold)" stroke-width="1.5">
        <path d="M30 80 V26 H70"/>
        <path d="M490 217 V271 H450"/>
        <path d="M420 26 H490 V70"/>
        <path d="M30 227 V271 H100"/>
      </g>
    </svg>
    <div class="brand">
      <span class="brand__dot"></span>
      <span class="brand__name">Harbourline Blinds &amp; Shutters</span>
    </div>
  </section>

</main>
</body>
</html>
```